Corvanto Card

The logo is the Spanish flag colors I want a vibrant eye catching design with the yellow / red colors over either Navy or white background or black even ,
Would like a 2D feel to the logo with another lighter color logo under it look ,

Contact Information for Business Card

Corvanto Flooring
Tobias Renwick
Main Number
Cell Number
Fax Number

Website on the side of the card somewhere

Font styles to use
Sans Serif

Colors
ec1f27
ffc214

Requirements
Must have
• 2 logos feel one is bolder and the other one underneath very light

```html
<!DOCTYPE html>
<html lang="en">
<head>
<meta charset="utf-8">
<title>Corvanto Card</title>
<link rel="stylesheet" href="https://fonts.googleapis.com/css2?family=Ubuntu:wght@400;500;700&display=swap">
<style>
  :root {
    --red: #ec1f27;
    --yellow: #ffc214;
    --gold: #e3b22a;
    --navy: #12184a;
    --white: #ffffff;
    --ink: #222222;
    --stage: #e9e7e3;
    --soft-peach: #f7c4ad;
    --soft-cream: #f5e3b8;
  }
  * { box-sizing: border-box; margin: 0; padding: 0; }
  html, body { width: 1200px; height: 675px; overflow: hidden; }
  body {
    background: var(--stage);
    font-family: "Ubuntu", sans-serif;
    position: relative;
  }
  .card {
    position: absolute;
    top: 183px;
    width: 540px;
    height: 309px;
    overflow: hidden;
    box-shadow: 0 6px 18px rgba(0,0,0,0.18);
  }
  .card--front { left: 40px; background: var(--white); }
  .card--back { left: 620px; background: var(--navy); }

  /* Front */
  .brand-mark {
    position: absolute;
    display: flex;
    align-items: center;
    gap: 8px;
  }
  .brand-mark__square { width: 14px; height: 14px; background: var(--red); flex: none; }
  .brand-mark__name {
    font-weight: 700;
    color: var(--gold);
    letter-spacing: 1.5px;
    line-height: 1.05;
    text-transform: uppercase;
  }
  .card--front .brand-mark { left: 34px; top: 40px; }
  .card--front .brand-mark__name { font-size: 20px; }

  .person { position: absolute; left: 34px; top: 118px; }
  .person__name { color: var(--red); font-weight: 700; font-size: 15px; text-transform: uppercase; }
  .person__role { color: var(--ink); font-size: 11px; margin-top: 2px; }

  .contacts { position: absolute; left: 34px; top: 165px; list-style: none; }
  .contacts__item {
    display: flex; align-items: center; gap: 8px;
    font-size: 13px; color: var(--ink); margin-bottom: 6px;
  }
  .contacts__icon {
    width: 14px; height: 14px; background: var(--red);
    display: flex; align-items: center; justify-content: center; flex: none;
  }
  .address {
    position: absolute; left: 200px; top: 244px; z-index: 1;
    font-size: 13px; color: var(--ink); line-height: 1.35;
    white-space: nowrap;
  }
  .corner-block { position: absolute; right: 0; bottom: 0; }

  /* Back */
  .card--back .stripes { position: absolute; left: 0; top: 0; }
  .card--back .brand-mark {
    left: 260px; top: 150px;
    flex-direction: column; gap: 10px;
  }
  .card--back .brand-mark__square { width: 22px; height: 22px; }
  .card--back .brand-mark__name { font-size: 26px; text-align: center; }
  .website {
    position: absolute; left: 205px; top: 245px;
    color: var(--gold); font-size: 15px; letter-spacing: 2px;
  }
</style>
</head>
<body>

<section class="card card--front" aria-label="Business card front">
  <div class="brand-mark">
    <span class="brand-mark__square"></span>
    <span class="brand-mark__name">Corvanto<br>Flooring</span>
  </div>

  <div class="person">
    <p class="person__name">Tobias Renwick</p>
    <p class="person__role">Managing Director</p>
  </div>

  <ul class="contacts">
    <li class="contacts__item">
      <span class="contacts__icon"><svg width="8" height="9" viewBox="0 0 8 9"><rect x="1.5" y="0.5" width="5" height="8" rx="1" fill="none" stroke="#fff"/></svg></span>
      0110 111 111
    </li>
    <li class="contacts__item">
      <span class="contacts__icon"><svg width="8" height="9" viewBox="0 0 8 9"><rect x="1.5" y="0.5" width="5" height="8" rx="1" fill="none" stroke="#fff"/></svg></span>
      2222 111 222
    </li>
    <li class="contacts__item">
      <span class="contacts__icon"><svg width="10" height="8" viewBox="0 0 10 8"><rect x="0.5" y="0.5" width="9" height="7" fill="none" stroke="#fff"/><path d="M0.5 0.5 L5 4.5 L9.5 0.5" fill="none" stroke="#fff"/></svg></span>
      info@corvantoflooring.com
    </li>
  </ul>

  <p class="address">Suite 102 Street name, State,<br>Zip 2034, Country</p>

  <svg class="corner-block" width="125" height="130" viewBox="0 0 125 130" aria-hidden="true">
    <rect x="30" y="0" width="95" height="40" fill="var(--soft-peach)"/>
    <rect x="0" y="55" width="125" height="75" fill="var(--soft-cream)"/>
  </svg>
</section>

<section class="card card--back" aria-label="Business card back">
  <svg class="stripes" width="220" height="309" viewBox="0 0 220 309" aria-hidden="true">
    <polygon points="110,0 150,0 40,309 0,309" fill="var(--red)"/>
    <polygon points="40,0 75,0 0,210 0,110" fill="var(--gold)"/>
  </svg>

  <div class="brand-mark">
    <span class="brand-mark__square"></span>
    <span class="brand-mark__name">Corvanto<br>Flooring</span>
  </div>

  <p class="website">www.corvantoflooring.com</p>
</section>

</body>
</html>
```